Brevora web site / landing page

Looking for design help with building a landing page for our company and possible the remaining site. We are an AI developer and customer software developer company. Uploading logos for color scheme attached in logo xip file.

Target Market(s)

Manufacturing, Small business, Sales

Coding

Coded - Design and coding required

Number of Pages Required

3 page

Colors

Designer to choose colors to be used in the design.

Requirements
Must have
• Landing page, additional pages for AI, Custom software and Customer Portals explanation.

```html
<!DOCTYPE html>
<html lang="en">
<head>
<meta charset="utf-8">
<title>Brevora Portals</title>
<link rel="stylesheet" href="https://fonts.googleapis.com/css2?family=Cinzel:wght@400;600;700&family=Lora:wght@600;700&family=Open+Sans:wght@400;600;700&display=swap">
<style>
:root{
  --blue:#1f74b8;
  --blue-dark:#175c95;
  --navy:#24358a;
  --ink:#1e2126;
  --text:#4a4f57;
  --muted:#8a9099;
  --line:#d9dde3;
  --paper:#ffffff;
  --soft:#f3f5f8;
  --dark:#15181d;
}
*{box-sizing:border-box;margin:0;padding:0}
html,body{width:1200px;height:3732px;overflow:hidden}
body{font-family:"Open Sans",Arial,sans-serif;color:var(--text);background:var(--paper);position:relative}
section,header,footer{position:relative;width:1200px;overflow:hidden}
.heading{font-family:"Cinzel",Georgia,serif;font-weight:600;color:var(--ink);text-align:center;font-size:40px;letter-spacing:2px}
.divider{display:flex;align-items:center;justify-content:center;gap:10px;margin:10px auto 0}
.divider span{width:56px;height:1px;background:var(--blue)}
.divider i{width:10px;height:10px;border:2px solid var(--blue);border-radius:50%}

/* hero */
.hero{height:620px;background:radial-gradient(circle at 78% 45%,#2d6f9e 0%,#163a5a 25%,#0b1624 55%,#05080d 100%)}
.hero-art{position:absolute;inset:0}
.nav{position:absolute;top:0;left:0;right:0;height:84px;display:flex;align-items:center;justify-content:space-between;padding:0 100px 0 48px}
.brand{display:flex;align-items:center;gap:12px;color:#fff;font-family:"Cinzel",Georgia,serif;font-size:22px;font-weight:600;letter-spacing:3px}
.brand i{width:26px;height:26px;border-radius:50%;background:#fff}
.nav ul{display:flex;list-style:none;gap:34px;font-size:15px;color:#fff}
.nav li.active{border-bottom:2px solid var(--blue);padding-bottom:6px}
.hero h1{position:absolute;left:66px;top:180px;width:560px;font-family:"Lora",Georgia,serif;font-weight:700;font-size:40px;line-height:52px;color:#fff}
.dots{position:absolute;bottom:34px;left:0;right:0;display:flex;justify-content:center;gap:10px}
.dots i{width:10px;height:10px;border-radius:50%;background:#9aa3ad}
.dots i:first-child{background:#fff}

/* about */
.about{height:412px}
.about-mark{position:absolute;left:150px;top:80px;width:248px;height:248px;border-radius:50%;border:8px solid var(--blue);display:flex;align-items:center;justify-content:center;font-family:"Open Sans",sans-serif;font-weight:700;font-size:34px;color:var(--blue)}
.about-body{position:absolute;left:488px;top:78px;width:600px}
.about-body .heading{text-align:left}
.about-body .divider{justify-content:flex-start;margin:10px 0 22px}
.about-lead{font-size:22px;line-height:32px;color:var(--ink);margin-bottom:22px}
.about-body p{font-size:15px;line-height:25px}

/* services */
.services{height:480px;background:linear-gradient(180deg,#2a2d33 0%,#1c1f24 100%)}
.services .photo{position:absolute;inset:0;background:linear-gradient(110deg,rgba(80,86,96,.55),rgba(30,33,38,.4) 50%,rgba(90,96,106,.5))}
.services .heading{color:#fff;padding-top:48px;position:relative}
.services .intro{position:relative;text-align:center;color:#d8dce2;font-size:14px;line-height:22px;width:480px;margin:20px auto 0}
.service-list{position:relative;display:flex;justify-content:center;gap:90px;margin-top:50px}
.service{width:220px;text-align:center;color:#e6e9ee}
.service svg{width:64px;height:64px;stroke:var(--blue);fill:none;stroke-width:2.5}
.service h3{font-size:16px;font-weight:700;color:#fff;margin:12px 0 8px}
.service p{font-size:12px;line-height:19px}

/* team */
.team{height:588px;background:var(--paper)}
.team .heading{padding-top:56px}
.team .intro{text-align:center;font-size:15px;line-height:26px;width:820px;margin:26px auto 0}
.lead-card{position:absolute;left:140px;top:260px;width:180px;height:288px;background:var(--blue);color:#fff;text-align:center;padding:28px 18px;box-shadow:0 8px 18px rgba(0,0,0,.2)}
.lead-card h4{font-family:"Cinzel",serif;font-size:22px}
.lead-card .role{font-size:12px;opacity:.9;margin:4px 0 14px}
.lead-card p{font-size:11px;line-height:18px}
.lead-card .btn{width:26px;height:26px;border-radius:50%;background:#fff;margin:16px auto 0}
.members{position:absolute;left:345px;top:268px;display:flex;gap:36px}
.member{width:140px;text-align:center}
.member .photo{width:128px;height:128px;margin:0 auto;border-radius:50%;border:5px solid var(--blue);background:linear-gradient(160deg,#c9ced6,#8e98a6)}
.member h4{font-family:"Cinzel",serif;font-size:20px;color:var(--ink);margin-top:18px}
.member .role{font-size:12px;color:var(--muted);margin-top:4px}
.member .btn{width:24px;height:24px;border-radius:50%;background:var(--blue);margin:14px auto 0}

/* why */
.why{height:640px;background:var(--soft)}
.why .heading{padding-top:76px}
.reasons{position:absolute;left:140px;top:170px;display:grid;grid-template-columns:repeat(3,280px);column-gap:40px;row-gap:40px}
.reason{height:196px;background:var(--paper);text-align:center;padding:20px 26px;box-shadow:0 4px 14px rgba(0,0,0,.08)}
.reason.blue{background:var(--blue);color:#fff}
.reason svg{width:44px;height:44px;stroke:var(--blue);fill:none;stroke-width:2}
.reason.blue svg{stroke:#fff}
.reason h4{font-family:"Cinzel",serif;font-size:17px;line-height:22px;color:var(--ink);margin:8px 0 8px}
.reason.blue h4{color:#fff}
.reason p{font-size:12px;line-height:18px}

/* contact */
.contact{height:620px;background:linear-gradient(135deg,#e4e6e9,#d3d6da 60%,#dcdfe2)}
.map{position:absolute;inset:0}
.talk{position:absolute;left:140px;top:80px;width:348px;height:440px;background:var(--paper);padding:40px 46px;box-shadow:0 10px 28px rgba(0,0,0,.2)}
.talk h2{font-family:"Cinzel",serif;font-size:34px;color:var(--ink)}
.talk .divider{justify-content:flex-start;margin:8px 0 22px}
.field{height:44px;border-bottom:1px solid var(--line);display:flex;align-items:center;gap:12px;font-size:13px;color:var(--muted)}
.field i{width:12px;height:12px;border-radius:50%;background:var(--blue)}
.field.tall{height:64px}
.submit{margin-top:26px;width:130px;height:40px;border-radius:20px;background:var(--navy);color:#fff;font-size:13px;font-weight:700;display:flex;align-items:center;justify-content:center;letter-spacing:1px}
.pin-card{position:absolute;left:972px;top:300px;width:190px;background:var(--paper);padding:12px 14px;font-size:11px;line-height:17px;color:var(--ink);box-shadow:0 4px 12px rgba(0,0,0,.2)}
.curve{position:absolute;left:0;bottom:0;width:1200px;height:80px}
.curve-mark{position:absolute;left:570px;bottom:8px;width:60px;height:60px;border-radius:50%;background:var(--paper);border:3px solid var(--blue)}

/* footer */
.footer{height:372px;background:var(--dark);color:#cfd3d9}
.footer .photo{position:absolute;inset:0;background:linear-gradient(100deg,#2a2e35,#16191e 50%,#262a31)}
.contacts{position:absolute;top:96px;left:0;right:0;display:flex;justify-content:center;gap:100px}
.contact-item{width:200px;text-align:center}
.contact-item svg{width:40px;height:40px;stroke:#fff;fill:none;stroke-width:2}
.contact-item h5{color:var(--blue);font-size:13px;letter-spacing:1px;margin:12px 0 8px}
.contact-item p{font-size:12px;line-height:19px}
.copyright{position:absolute;bottom:0;left:0;right:0;height:44px;border-top:1px solid #30343b;text-align:center;line-height:44px;font-size:12px;color:#8a9099}
</style>
</head>
<body>

<header class="hero">
  <div class="hero-art" role="img" aria-label="Hand touching a glowing digital network globe"></div>
  <nav class="nav">
    <div class="brand"><i></i>Brevora Portals</div>
    <ul>
      <li class="active">Home</li><li>About Us</li><li>Services</li><li>The Team</li><li>Contact Us</li>
    </ul>
  </nav>
  <h1>We are an AI developer and customer software developer company.</h1>
  <div class="dots"><i></i><i></i><i></i><i></i></div>
</header>

<section class="about">
  <div class="about-mark">Brevora</div>
  <div class="about-body">
    <h2 class="heading">About Us</h2>
    <div class="divider"><span></span><i></i><span></span></div>
    <p class="about-lead">Lorem ipsum dolor sit amet, consectetuer adipiscing elit, sedda nonummy nibh euismod tincidunt ut laoreet dolore.</p>
    <p>Lorem ipsum dolor sit amet, enim ad minim veniam, quis nostrud exerci tation ullamcorper suscipit lobortis nisl ut aliquip ex ea commodo consequat. Duis autem vel eum iriure dolor in hendrerit in vulputate velit esse molestie consequat, vel illum dolore eu feugiat nulla facilisis at vero eros et accumsan et.</p>
  </div>
</section>

<section class="services">
  <div class="photo" role="img" aria-label="Developers working at computers in an office"></div>
  <h2 class="heading">Our Services</h2>
  <div class="divider" style="position:relative"><span></span><i></i><span></span></div>
  <p class="intro">Lorem ipsum dolor sit amet, consectetuer adipiscing elit sedda nonummy nibh euismod tincidunt.</p>
  <div class="service-list">
    <div class="service">
      <svg viewBox="0 0 64 64"><rect x="12" y="14" width="40" height="28" rx="2"/><path d="M24 50h16M32 42v8M22 28h20"/></svg>
      <h3>AI Developer</h3>
      <p>Lorem ipsum dolor sit amet consectetuer adipiscing elit sed diam nonummy nibh euismod.</p>
    </div>
    <div class="service">
      <svg viewBox="0 0 64 64"><rect x="8" y="12" width="48" height="34" rx="2"/><path d="M26 24l-6 6 6 6M38 24l6 6-6 6M22 54h20"/></svg>
      <h3>Custom Software Developer</h3>
      <p>Lorem ipsum dolor sit amet consectetuer adipiscing elit sed diam nonummy nibh euismod.</p>
    </div>
    <div class="service">
      <svg viewBox="0 0 64 64"><rect x="10" y="10" width="44" height="44" rx="3"/><path d="M10 22h44M20 32h24M20 42h16"/></svg>
      <h3>Customer Portals Explanation</h3>
      <p>Lorem ipsum dolor sit amet consectetuer adipiscing elit sed diam nonummy nibh euismod.</p>
    </div>
  </div>
</section>

<section class="team">
  <h2 class="heading">The Team</h2>
  <div class="divider"><span></span><i></i><span></span></div>
  <p class="intro">Our developers use the latest tech, including Corvix and LinkStream, while ensuring the creative freedom of open-source programs and fully customizable toolkits. We're proud to be a unique team offering.</p>
  <div class="lead-card">
    <h4>Corin</h4>
    <p class="role">Customer Manager</p>
    <p>Lorem ipsum dolor sit amet consectetuer adipiscing elit sed diam nonummy nibh euismod tincidunt ut laoreet dolore magna.</p>
    <div class="btn"></div>
  </div>
  <div class="members">
    <div class="member"><div class="photo" role="img" aria-label="Portrait of team member Dorian"></div><h4>Dorian</h4><p class="role">Client Success Manager</p><div class="btn"></div></div>
    <div class="member"><div class="photo" role="img" aria-label="Portrait of team member Emilio"></div><h4>Emilio</h4><p class="role">Systems Administration</p><div class="btn"></div></div>
    <div class="member"><div class="photo" role="img" aria-label="Portrait of team member Tarek"></div><h4>Tarek</h4><p class="role">Client Success Manager</p><div class="btn"></div></div>
    <div class="member"><div class="photo" role="img" aria-label="Portrait of team member Rowan"></div><h4>Rowan</h4><p class="role">Client Success Manager</p><div class="btn"></div></div>
  </div>
</section>

<section class="why">
  <h2 class="heading">Why Choose Us</h2>
  <div class="divider"><span></span><i></i><span></span></div>
  <div class="reasons">
    <div class="reason"><svg viewBox="0 0 46 46"><circle cx="23" cy="15" r="8"/><path d="M8 42c2-10 28-10 30 0"/></svg><h4>Certified Experts</h4><p>Lorem ipsum dolor sit amet consectetuer adipiscing elit sed nonummy.</p></div>
    <div class="reason blue"><svg viewBox="0 0 46 46"><circle cx="23" cy="23" r="17"/><path d="M23 12v11l7 5"/></svg><h4>24/7 Services</h4><p>Lorem ipsum dolor sit amet consectetuer adipiscing elit sed nonummy.</p></div>
    <div class="reason"><svg viewBox="0 0 46 46"><path d="M6 22h8v18H6zM14 24l8-14c4 0 5 3 4 8h12c3 0 4 3 3 5l-4 14H14"/></svg><h4>Satisfied Clients</h4><p>Lorem ipsum dolor sit amet consectetuer adipiscing elit sed nonummy.</p></div>
    <div class="reason blue"><svg viewBox="0 0 46 46"><rect x="14" y="14" width="18" height="18"/><path d="M19 6v8M27 6v8M19 32v8M27 32v8M6 19h8M6 27h8M32 19h8M32 27h8"/></svg><h4>Latest Technology</h4><p>Lorem ipsum dolor sit amet consectetuer adipiscing elit sed nonummy.</p></div>
    <div class="reason"><svg viewBox="0 0 46 46"><rect x="6" y="14" width="34" height="24" rx="2"/><path d="M17 14V8h12v6M6 24h34"/></svg><h4>Years Of Experience</h4><p>Lorem ipsum dolor sit amet consectetuer adipiscing elit sed nonummy.</p></div>
    <div class="reason blue"><svg viewBox="0 0 46 46"><circle cx="23" cy="23" r="17"/><path d="M28 16h-7a4 4 0 000 8h4a4 4 0 010 8h-8M23 12v4M23 32v4"/></svg><h4>Our Prices are Affordable</h4><p>Lorem ipsum dolor sit amet consectetuer adipiscing elit sed nonummy.</p></div>
  </div>
</section>

<section class="contact">
  <div class="map" role="img" aria-label="Street map showing the office location"></div>
  <div class="talk">
    <h2>Let's Talk</h2>
    <div class="divider"><span></span><i></i><span></span></div>
    <div class="field"><i></i>Name</div>
    <div class="field"><i></i>Phone</div>
    <div class="field"><i></i>Email</div>
    <div class="field tall"><i></i>Message</div>
    <div class="submit">SUBMIT</div>
  </div>
  <div class="pin-card">48 Harbor Row, Suite 5,<br>Westbrook ME 04092</div>
  <svg class="curve" viewBox="0 0 1200 80" preserveAspectRatio="none"><path d="M0 80 Q600 -10 1200 80Z" fill="#15181d"/></svg>
  <div class="curve-mark"></div>
</section>

<footer class="footer">
  <div class="photo" role="img" aria-label="Person typing on a laptop in a dim workspace"></div>
  <div class="contacts">
    <div class="contact-item">
      <svg viewBox="0 0 40 40"><path d="M20 36s-11-12-11-20a11 11 0 0122 0c0 8-11 20-11 20z"/><circle cx="20" cy="16" r="4"/></svg>
      <h5>ADDRESS</h5><p>48 Harbor Row, Suite 5,<br>Westbrook ME 04092</p>
    </div>
    <div class="contact-item">
      <svg viewBox="0 0 40 40"><rect x="11" y="4" width="18" height="32" rx="3"/><path d="M18 31h4"/></svg>
      <h5>PHONE</h5><p>555 018 2046</p>
    </div>
    <div class="contact-item">
      <svg viewBox="0 0 40 40"><rect x="4" y="9" width="32" height="22" rx="2"/><path d="M4 10l16 12 16-12"/></svg>
      <h5>EMAIL</h5><p>hello@brevora.example</p>
    </div>
  </div>
  <div class="copyright">Copyright © 2020 Brevora Portals. All Rights Reserved.</div>
</footer>

</body>
</html>
```